Desert Basin Company Brochure

**** UPDATE 2-8-2014 ****

Size should be 11" X 17" or larger (tri or bi fold).

We're going to let the contest run it's full duration to allow for more time spent on designs.

No black backgrounds.

Consideration should be given to having the text be easy to read and in a nice, organized format.

*****************************

We're looking for an eye-catching, colorful brochure that will explain what we do, who we are... and what sets us apart from the competition.

Our company provides swimming pool service, repair, and custom renovations throughout the Phoenix, Arizona metropolitan area. These brochures will be hand-delivered to each prospective customer we visit.

The brochure will include images of our work, product logos, and a unique design that separates our company apart from the rest.

The brochure should be tri-fold. Although, if a designer wants to (or has better ideas) for a different lay-out, then we're open to seeing what can be done.

Colors we like: Blue, White, Silver, Copper, Green (accent color)

We like designs that are unique/different. Professional. Creative. Sleek. Sexy. Custom. We don't want the brochure to be "pretentious". We'd like for these brochures to leave a lasting impression with our prospective clients... and hopefully earn us more business.

We don't want the brochure to be too wordy, however if the designer feels we need to cut back (or add), let us know.

Our motto is "Every Ripple Counts Twice".

You can view some of our projects, and what we're about either at our website (brightwaveaqua.example), Chatterbook (www.facebook/brightwaveaqua), or Searchly+ (https://plus.google.com/+Brightwaveaqua). Thank you!

- Print-

(Front) Logo

Service - Repair - Renovation
555-731-4409
brightwaveaqua.example
service@brightwaveaqua.example
Like Us On Chatterbook! Chatterbook LOGO
Searchly Plus LOGO

(Body) Why Choose Us?

Thank you for the opportunity for our company to become your pool service provider!

We’re committed to providing the best customer service possible! At the end of the day you want your pool to be clean, clear, operational, and for your service provider to be available when you need them!

We’re licensed with the Westland Board Of Tradesmen, Bonded, and Fully Insured.
A+ reviews with the Honest Trade Council, Marla’s Picks, Wombit, Vyn, Chatterbook, and Searchly!
All technicians are employees... not sub-contractors! Our employees are hard working, dependable, professional, and expected to follow our strict protocol for servicing your pool.
Flat-fee service rates! Any additional equipment repairs, maintenance, or chemical implementations are directly authorized by you!
No contracts! Our Service Level Agreement Form allows you to select your desired level of authorization for equipment repairs, filter maintenance, and extra chemical implementation programs.
Our uniformed technicians arrive in distinctive, clean GPS-tracked company trucks.
We leave detailed service slips after each service visit. In addition, all service visit information is electronically recorded and stored.
Easy, online account management to view and pay invoices or authorize estimates.
Invoices, estimates, questions, pictures, and video are communicated via e-mail!
Free service calls to diagnose equipment issues outside of our normal service.
10% Service Client Discount for all repairs and replacement items.
Brightwave Aqua knows the importance of communication! We’re available by phone, email, or text all days of the week.

(Body) Our Methodology

We believe in 5 important factors in maintaining a clean, clear, and operational pool...

Good, Clean Water! Our local water supply contains high amounts of minerals. Pool chemicals add to this problem in a short amount of time. Our philosophy is to use the least amount of chemicals possible to achieve optimal water balance.
Efficient Water Flow! The invention of variable-speed pumps has enabled the ability to "dial in" proper water flow... while driving down energy costs.
Proper Filtration! Today’s high-capacity cartridge filters provide great filtration, save on wasted water from backwashing sand filters, and eliminate the need for water flow-restricting backwash valves.
Functioning Cleaning System! Having a working automatic cleaning system is vital in keeping the pool surface clean of debris and dirt... and free of staining.
A Dependable And Professional Pool Maintenance Technician! Our job is to not only oversee all of the items listed above... but to make sure your pool is in the best condition possible!

(Body) Equipment Repair & Installation

We’re educated on all phases of swimming pool equipment repair and installation... with a focus on energy-efficiency and optimum performance!

We’re an KTV & MWE Authorized Installer of variable-speed pool pumps. KTV & MWE trust us to properly install and calibrate all variable-speed pumps. We've been equipped to handle the new industry standards on variable-speed pumps since Arizona law went into effect January 1st, 2011.
We’re experts at acid washes and erasing the mineral build-up off of waterlines. All work is done in-house with our customized cleaning rig and trailer.
Heating systems. New efficiency standards have made installation and operation more affordable than ever.
Remote control automation systems. Technology now allows the user to easily view and control their entire pool system via a remote home computer, tablet, or phone!
Brilliant, color-changing LED lighting for pools and spas! The benefits of LED include brighter and broader displays... while lasting much longer than your typical light bulbs.
Salt systems provide a soft-water experience! In addition to the benefit of better feeling water, salt systems generate plenty of chlorine to keep your pool sanitized.

(Body) About Us

A native to Phoenix, Dorian Kessel founded Brightwave Aqua in 2000. Our company was built from the ground up by way of hard work, word of mouth, and determination. Our company will always remain firmly grounded, and continue to develop systems that put our customers first!

Our philosophy is to treat every pool as if it were our own, run an efficient and organized business, and care for our employees.

Brightwave Aqua is a yearly, proud contributor to the Saguaro Youth Medical Center Splash Smart Day. Please educate and watch all children around water... every accident can be avoided.

(Back) Contact Us
Logos To Use, Files Uploaded: Marla’s Picks, HTC, Hydrova, Searchly+, Chatterbook, KTV/MWE logo, Saguaro Youth Medical Center

Office: 555-731-4409 | Fax: 555-731-4413 | Email: service@brightwaveaqua.example
brightwaveaqua.example

Office / Warehouse Location
41276 East Cholla Street, Suite 8
Phoenix, Arizona 85999
(NW of Cholla Street & Ironwood Mesa Road)

AZ ROC: 731502, 731503, 731504, 864017

Target Market(s)

We target a market of pool owners, which typically have more disposable income.

30 - 75 years old.

Our clients range from first-time home buyers, self-employed, business professionals, doctors, landlords, thousandaires, millionaires.

Industry/Entity Type

Pool Service

Font styles to use
Serif

Colors
0355a3
cfdfed
ffffff
3176b5
eaf1f7

Requirements
Must have
• Must use provided images. We've included a few pool pictures, and will let you decide which ones to incorporate throughout the brochure.

Logos Used:
Brightwave Aqua
Hydrova
HTC
Marla's Picks
KTV
MWE
Saguaro Youth Medical Center
Searchly+
Chatterbook

Image pic of some of our trucks.

Nice to have
• Equipment images worked in.
Should not have
• Cartoonish fonts or design. No "Love" hearts!!

```html
<!DOCTYPE html>
<html lang="en">
<head>
<meta charset="utf-8">
<title>Desert Basin Company Brochure – Inside Spread</title>
<link rel="stylesheet" href="https://fonts.googleapis.com/css2?family=Source+Sans+3:wght@400;600;700&display=swap">
<style>
  :root {
    --brand-blue: #0355a3;
    --mid-blue: #3176b5;
    --pale-blue: #cfdfed;
    --mist: #eaf1f7;
    --white: #ffffff;
    --ink: #1d1d1d;
    --body: #4a4a4a;
    --accent-green: #7dc242;
  }
  * { box-sizing: border-box; margin: 0; padding: 0; }
  html, body { width: 1200px; height: 777px; overflow: hidden; background: var(--white); }
  body { font-family: "Source Sans 3", "Myriad Pro", Arial, sans-serif; color: var(--body); }

  .spread { position: relative; width: 1200px; height: 777px; background: var(--white); overflow: hidden; }
  .wave { position: absolute; left: 0; width: 1200px; }
  .wave--top { top: 0; height: 40px; z-index: 3; }
  .wave--bottom { bottom: 0; height: 90px; z-index: 3; }
  .fold { position: absolute; top: 0; bottom: 0; width: 1px; background: #e4e8ec; z-index: 1; }

  .photo { position: absolute; z-index: 2; }
  .photo--rock-pool { left: 22px; top: 470px; width: 350px; height: 260px;
    background: linear-gradient(170deg, #5f8f55 0%, #b8a88a 35%, #5fb6c4 65%, #2d8aa3 100%); }
  .photo--crew { left: 428px; top: 6px; width: 338px; height: 168px;
    background: linear-gradient(180deg, #a8b5b8 0%, #8f7f66 35%, #2e8a91 75%, #c6c4bd 100%); }
  .photo--stone-spa { left: 372px; top: 562px; width: 446px; height: 200px;
    background: linear-gradient(180deg, #a88a6a 0%, #7a6553 45%, #5b4a3d 70%, #3f8aa6 100%); }
  .photo--infinity { left: 818px; top: 435px; width: 360px; height: 160px;
    background: linear-gradient(180deg, #b9c7cf 0%, #c7ad84 30%, #2f6fa0 60%, #6d6352 100%); }
  .photo--grotto { left: 818px; top: 595px; width: 360px; height: 140px;
    background: linear-gradient(180deg, #4f7f48 0%, #9a8f7a 45%, #5fb0c0 75%, #d8d4cc 100%); }

  h2 { font-weight: 700; color: var(--ink); font-size: 23px; line-height: 1.1; }
  p, li { font-size: 13.5px; line-height: 16.5px; }
  strong { color: var(--ink); font-weight: 700; }

  .methodology { position: absolute; left: 16px; top: 38px; width: 372px; z-index: 4; }
  .methodology h2 { text-align: center; margin-bottom: 4px; }
  .methodology .lead { font-weight: 700; color: var(--ink); padding-left: 30px; margin-bottom: 5px; }
  .factor-list { list-style: none; }
  .factor { position: relative; padding-left: 30px; margin-bottom: 3px; }
  .factor-num { position: absolute; left: 0; top: 0; width: 22px; height: 22px; border-radius: 50%;
    background: var(--accent-green); color: var(--ink); font-weight: 700; font-size: 13px;
    display: flex; align-items: center; justify-content: center; }

  .equipment { position: absolute; left: 426px; top: 182px; width: 350px; z-index: 4; }
  .equipment h2 { margin-bottom: 4px; }
  .about { position: absolute; left: 428px; top: 265px; width: 346px; z-index: 4; }
  .about h2 { text-align: center; margin-bottom: 3px; }
  .about p { padding-left: 2px; }
  .about .gap { margin-top: 9px; }

  .installs { position: absolute; left: 836px; top: 40px; width: 336px; z-index: 4; }
  .installs p + p { margin-top: 8px; }

  .heating { position: absolute; left: 818px; top: 158px; width: 360px; height: 275px; z-index: 2;
    padding: 6px 16px 0 16px; color: var(--white);
    background: linear-gradient(180deg, #1f2a6b 0%, #2c3d86 40%, #3b2f6e 75%, #4d4f7a 100%); }
  .heating h3 { text-align: center; color: var(--accent-green); font-size: 23px; font-weight: 700; line-height: 28px; }
  .heating p { color: var(--white); font-size: 13.5px; line-height: 16.5px; }
</style>
</head>
<body>
<main class="spread">

  <svg class="wave wave--top" viewBox="0 0 1200 40" preserveAspectRatio="none" aria-hidden="true">
    <path d="M0 0 H1200 V22 C1100 10 1000 30 900 24 C820 18 800 8 760 12 C640 22 520 6 400 14 C300 20 200 4 0 12 Z" fill="#0355a3"/>
    <path d="M0 12 C200 4 300 20 400 14 C520 6 640 22 760 12 C800 8 820 18 900 24 C1000 30 1100 10 1200 22 V28 C1100 18 1000 38 900 32 C800 26 780 16 760 20 C640 30 520 14 400 22 C300 28 200 12 0 20 Z" fill="#cfdfed"/>
  </svg>

  <div class="fold" style="left:400px"></div>
  <div class="fold" style="left:800px"></div>

  <section class="methodology">
    <h2>Our Methodology</h2>
    <p class="lead">We believe in 5 important factors in maintaining a clean, clear, and operational pool...</p>
    <ol class="factor-list">
      <li class="factor"><span class="factor-num">1</span><strong>Good, Clean Water!</strong> Our local water supply contains high amounts of minerals. Pool chemicals add to this problem in a short amount of time. Our philosophy is to use the least amount of chemicals possible to achieve optimal water balance.</li>
      <li class="factor"><span class="factor-num">2</span><strong>Efficient Water Flow!</strong> The invention of variable-speed pumps has enabled the ability to "dial in" proper water flow... while driving down energy costs.</li>
      <li class="factor"><span class="factor-num">3</span><strong>Proper Filtration!</strong> Today’s high-capacity cartridge filters provide great filtration, save on wasted water from backwashing sand filters, and eliminate the need for water flow-restricting backwash valves.</li>
      <li class="factor"><span class="factor-num">4</span><strong>Functioning Cleaning System!</strong> Having a working automatic cleaning system is vital in keeping the pool surface clean of debris and dirt... and free of staining.</li>
      <li class="factor"><span class="factor-num">5</span><strong>A Dependable And Professional Pool Maintenance Technician!</strong> Our job is to not only oversee all of the items listed above... but to make sure your pool is in the best condition possible!</li>
    </ol>
  </section>

  <div class="photo photo--rock-pool" role="img" aria-label="Photo of a rock-edged pool with waterfall and spa"></div>

  <div class="photo photo--crew" role="img" aria-label="Photo of technicians acid-washing an empty pool with the cleaning rig and trailer"></div>

  <section class="equipment">
    <h2>Equipment Repair &amp; Installation</h2>
    <p>We’re educated on all phases of swimming pool equipment repair and installation... with a focus on energy-efficiency and optimum performance!</p>
  </section>

  <section class="about">
    <h2>About Us</h2>
    <p>A native to Phoenix, Dorian Kessel founded Brightwave Aqua in 2000. Our company was built from the ground up by way of hard work, word of mouth, and determination. Our company will always remain firmly grounded, and continue to develop systems that put our customers first!</p>
    <p>Our philosophy is to treat every pool as if it were our own, run an efficient and organized business, and care for our employees.</p>
    <p>Brightwave Aqua is a yearly, proud contributor to the Saguaro Youth Medical Center Splash Smart Day. Please educate and watch all children around water... every accident can be avoided.</p>
    <p class="gap">We’re an KTV &amp; MWE Authorized Installer of variable-speed pool pumps. KTV &amp; MWE trust us to properly install and calibrate all variable- speed pumps.</p>
  </section>

  <div class="photo photo--stone-spa" role="img" aria-label="Photo of a stacked-stone spa with a sheer water spillway"></div>

  <section class="installs">
    <p>We've been equipped to handle the new industry standards on variable-speed pumps since Arizona law went into effect January 1st, 2011.</p>
    <p>We’re experts at acid washes and erasing the mineral build-up off of waterlines. All work is done in-house with our customized cleaning rig and trailer.</p>
  </section>

  <section class="heating" role="group" aria-label="Pool systems over a dusk pool photo">
    <h3>Heating system</h3>
    <p>New efficiency standards have made installation and operation more affordable than ever.</p>
    <p>Remote control automation systems.</p>
    <p>Technology now allows the user to easily view and control their entire pool system via a remote home computer, tablet, or phone!</p>
    <p>Brilliant, color-changing LED lighting for pools and spas! The benefits of LED include brighter and broader displays... while lasting much longer than your typical light bulbs.</p>
    <p>Salt systems provide a soft-water experience! In addition to the benefit of better feeling water, salt systems generate plenty of chlorine to keep your pool sanitized.</p>
  </section>

  <div class="photo photo--infinity" role="img" aria-label="Photo of a desert infinity-edge pool"></div>
  <div class="photo photo--grotto" role="img" aria-label="Photo of a rock grotto pool with round spa"></div>

  <svg class="wave wave--bottom" viewBox="0 0 1200 90" preserveAspectRatio="none" aria-hidden="true">
    <path d="M0 40 C120 60 260 62 400 52 C520 44 600 70 760 76 C900 80 1000 40 1200 20 V90 H0 Z" fill="#ffffff"/>
    <path d="M0 55 C120 72 260 74 400 64 C520 56 600 80 760 84 C900 88 1000 52 1200 36 V90 H0 Z" fill="#3176b5"/>
    <path d="M0 66 C140 80 280 82 420 74 C540 66 640 88 800 88 C940 88 1040 64 1200 52 V90 H0 Z" fill="#0355a3"/>
  </svg>

</main>
</body>
</html>
```